Vantor Hub Portal Page . It's guarantee project!

We need a clean and professional modern web application portal page
That includes the Login & Application Selection screen

Also, I need to design both Desktop and Mobile sizes.
We have an example design for our target

The application is Jetty Schedule and related data.
Our client is a bit conservative.

Theme color preferred : #00508B (main) #DF0D83 (secondary)

Target Market(s)

Oil & Fuel & Gasoline

Number of Pages Required

2 page

Font styles to use
Sans Serif

Colors
0054AA
0677BA
7BADD7
CADEEF
E8F1F8
E54698
E96AAD
F1A4CE
F9D9EA
FCEFF6

Requirements
Must have
• Login Page & Main Screen

```html
<!DOCTYPE html>
<html lang="en">
<head>
<meta charset="utf-8">
<title>Vantor Hub – Portal</title>
<link href="https://fonts.googleapis.com/css2?family=Lato:wght@400;700&family=Raleway:wght@400;700&display=swap" rel="stylesheet">
<style>
:root{
  --brand:#00508B;
  --accent:#DF0D83;
  --card-bg:#FCEFF6;
  --card-border:#F1A4CE;
  --white:#ffffff;
}
*{margin:0;padding:0;box-sizing:border-box}
html,body{width:1200px;height:928px;overflow:hidden;background:var(--white);font-family:'Lato',sans-serif}
.topbar{position:absolute;left:0;top:0;width:1200px;height:83px;background:var(--brand);color:var(--white)}
.brand{position:absolute;left:45px;top:26px;font-family:'Lato',sans-serif;font-weight:700;font-size:25px;color:#e6eef6}
.user{position:absolute;right:113px;top:23px;text-align:right;font-size:13px;line-height:21px}
.avatar{position:absolute;left:1102px;top:19px}
.hero{position:absolute;left:34px;top:108px;width:1131px;height:363px;border-radius:40px;overflow:hidden;
  background:linear-gradient(120deg,#b0306e 0%,#c9457f 30%,#8a3a8e 60%,#6a3e96 100%)}
.hero-title{position:absolute;left:0;right:0;top:136px;text-align:center;color:var(--white);font-weight:700;font-size:37px}
.hero-sub{position:absolute;left:0;right:0;top:205px;text-align:center;color:var(--white);font-size:19px}
.nav{position:absolute;top:162px}
.nav.prev{left:38px}.nav.next{left:1060px}
.dots{position:absolute;left:523px;top:321px;display:flex;gap:9px}
.dot{width:14px;height:14px;border-radius:50%;border:1.5px solid var(--white)}
.dot.active{background:var(--white)}
.hero-badge{position:absolute;left:964px;top:197px;width:167px;height:166px;background:var(--accent);border-top-left-radius:16px}
.apps{position:absolute;left:35px;top:523px;display:flex;gap:23px}
.app-card{position:relative;width:361px;height:367px;background:var(--card-bg);border:1.5px solid var(--card-border);border-radius:16px}
.app-art{position:absolute;left:85px;top:32px;width:190px;height:190px;border-radius:20px;background:radial-gradient(circle,#f3c9b8 0%,#9fcbe0 60%,var(--card-bg) 100%)}
.app-name{position:absolute;left:32px;top:252px;font-family:'Raleway',sans-serif;color:var(--brand);font-size:39px;line-height:44px}
.app-name b{display:block;font-weight:700}
.app-name span{display:block;font-weight:400}
.chev{position:absolute;left:296px;top:307px}
</style>
</head>
<body>
<header class="topbar">
  <div class="brand">Vantor Hub</div>
  <div class="user"><div>Mara Lind</div><div>mara.lind@example.com</div></div>
  <svg class="avatar" width="72" height="46" viewBox="0 0 72 46">
    <circle cx="22" cy="22" r="20.5" fill="none" stroke="#fff" stroke-width="2.5"/>
    <circle cx="22" cy="17" r="7" fill="none" stroke="#fff" stroke-width="2.5"/>
    <path d="M8 34c6-8 22-8 28 0" fill="none" stroke="#fff" stroke-width="2.5"/>
    <path d="M55 18h15l-7.5 9z" fill="#fff"/>
  </svg>
</header>

<section class="hero" role="img" aria-label="Aerial photo of a container ship docked at a jetty with cranes, in pink and purple tones">
  <h1 class="hero-title">Welcome to Jetty Schedule Portal</h1>
  <p class="hero-sub">Manage your schedules and related data efficiently.</p>
  <svg class="nav prev" width="34" height="40" viewBox="0 0 34 40"><path d="M18 2L2 20l16 18M30 2L14 20l16 18" fill="none" stroke="#fff" stroke-width="2"/></svg>
  <svg class="nav next" width="34" height="40" viewBox="0 0 34 40"><path d="M4 2l16 18L4 38M16 2l16 18-16 18" fill="none" stroke="#fff" stroke-width="2"/></svg>
  <div class="dots"><span class="dot active"></span><span class="dot"></span><span class="dot"></span><span class="dot"></span></div>
  <div class="hero-badge" role="img" aria-label="Brand emblem area"></div>
</section>

<main class="apps">
  <a class="app-card">
    <div class="app-art" role="img" aria-label="Illustration of a ship beside a calendar and map pin"></div>
    <div class="app-name"><b>Jetty</b><span>Planning</span></div>
    <svg class="chev" width="22" height="36" viewBox="0 0 22 36"><path d="M2 2l17 16L2 34" fill="none" stroke="#00508B" stroke-width="2"/></svg>
  </a>
  <a class="app-card">
    <div class="app-art" role="img" aria-label="Illustration of a ship in front of a globe"></div>
    <div class="app-name"><b>Jetty</b><span>Tracking</span></div>
    <svg class="chev" width="22" height="36" viewBox="0 0 22 36"><path d="M2 2l17 16L2 34" fill="none" stroke="#00508B" stroke-width="2"/></svg>
  </a>
  <a class="app-card">
    <div class="app-art" role="img" aria-label="Illustration of a large ship sailing on waves"></div>
    <div class="app-name"><b>Jetty</b><span>Performance</span></div>
    <svg class="chev" width="22" height="36" viewBox="0 0 22 36"><path d="M2 2l17 16L2 34" fill="none" stroke="#00508B" stroke-width="2"/></svg>
  </a>
</main>
</body>
</html>
```